Bwerani Ridge coffee needs bold, new coffee pack design

Having just developed a new logo (see attached file), we are now in the process of developing new coffee bag packaging designs. We are using a custom bag printer in the US, so the design will need will need to follow a specific art spec/template (which has also been uploaded). We will eventually need designs for two different coffee brands/types and two different size bags (essentially a 250g and 500g size). At this point, however, our goal is to develop a design for one size/coffee brand and from there work on variations for the others.
Updates

Project Deadline Extended
Reason: We are considering some small changes to the original design we outlined and want to allow extra time for current and new designers to make those tweaks. Thanks for your consideration of our coffee package project!

Hello, After reviewing some designs so far, and receiving additional feedback from test users in our market, we are making some changes to the template design. I have uploaded a new version of the template content, which has the following changes. 1. The two side panels are now without any text, but a visual design/pattern that you want to try there is still welcome. 2. The front and bag sections has been cleaned up a bit to have less text and more room for a visual design. 3. We would like to see stronger user of the following colors: red, yellow, black (which are Ugandan flag colors) and white. Some green as needed is allowed. 4. I have uploaded a map file showing Uganda including the Bwerani region where the coffee comes from. Would like to incorporate this on the back side, ideally with a small Bwerani Ridge logo pointing to the region in the bottom left in green or could even say something like "Home of Bwerani Ridge Coffee.". Also the country should be titled "Uganda" to make that clear. With these changes, if you need more time on the design, let me know and we can look at extending the deadline. Thank you!

Hello, Although it is not showing just yet, we expect to have a one-week extension for this contest (so not ending on 29 September, but October 6). If you are working on a design, or re-design, please continue to do so as the contest will be extended. If you are interested in starting work, please do so. Thanks for your interest in our package design contest and I look forward to seeing your work soon. Dalton

Hello, Thank you to everyone who has submitted designs so far. We want to highlight two important items at this point: 1. Based on user feedback, we are changing the design considerations bit. The size and shape of the bags are not changing, but some of the creative content is. A new file has been uploaded entitled Coffee package content 250g size v3.pdf which details these changes. Please download and read that for updates. If you have any questions, please let me know. 2. Due to these changes, we are extending this contest for another week, so I'm hopeful you will have time to make changes and submit your new ideas! Thank you, Dalton

Target Market(s)

Bwerani Ridge is a premium Ugandan coffee. We are targeting those drinkers who appreciate and seek out great coffee.

Industry/Entity Type

Printer

Font styles to use
Sans Serif

Colors
ec1f27
ffffff
9bcb3c
ffcf3e

Requirements
Must have
• The attached PDF file (coffee package content) design and content elements that need to be included. Designer has strong license to determine HOW they should be designed and shown. In terms of colors, would like to see strong use of red, black, yellow (Ugandan flag colors) and white. Green is also an option if needed.

The design file will need to follow specs that are detailed here:
http://www.packvello.com/artwork_specs and be in the format shown in the uploaded file 5-8 oz Bag Template.pdf.
Nice to have
• Bag should be simple, but elegant. We did testing and found that too much information was distracting so we have pared down the design/content elements to the basics. Still, creative elements or patterns and overlays are very welcome.
Should not have
• The tone should be elegant and creative, but not hokey or too handmade looking. Watch the use of too many fonts and low-contrast colors with text on background.

```html
<!DOCTYPE html>
<html lang="en">
<head>
<meta charset="utf-8">
<title>Bwerani Ridge — Coffee Bag Fronts</title>
<link href="https://fonts.googleapis.com/css2?family=Archivo+Black&family=Roboto:ital,wght@0,400;0,700;0,900;1,400&display=swap" rel="stylesheet">
<style>
  :root {
    --canvas-bg: #e9e9e9;
    --bag-top: #f6f3f1;
    --flag-red: #ec1f27;
    --flag-yellow: #ffcf3e;
    --flag-black: #161616;
    --white: #ffffff;
    --dark-land-light: #d6d0cd;
    --dark-land-mid: #6f625c;
    --dark-land-deep: #2a1d18;
    --light-land-light: #eee4dc;
    --light-land-mid: #a98466;
    --light-land-deep: #6b4429;
  }
  * { box-sizing: border-box; margin: 0; padding: 0; }
  html, body { width: 1200px; height: 957px; overflow: hidden; }
  body {
    background: var(--canvas-bg);
    font-family: "Roboto", Arial, sans-serif;
    position: relative;
  }
  .bag {
    position: absolute;
    top: 160px;
    width: 300px;
    height: 595px;
    background: var(--bag-top);
    overflow: hidden;
    box-shadow: 0 6px 18px rgba(0,0,0,.18);
  }
  .bag--dark { left: 268px; }
  .bag--light { left: 650px; }
  .bag__landscape {
    position: absolute;
    left: 0; right: 0; top: 130px; bottom: 0;
  }
  .bag--dark .bag__landscape {
    background: linear-gradient(180deg, var(--bag-top) 0%, var(--dark-land-light) 14%, var(--dark-land-mid) 48%, var(--dark-land-deep) 100%);
  }
  .bag--light .bag__landscape {
    background: linear-gradient(180deg, var(--bag-top) 0%, var(--light-land-light) 14%, var(--light-land-mid) 55%, var(--light-land-deep) 100%);
  }
  .bag__stripe {
    position: absolute;
    left: 0; right: 0; bottom: 0;
    height: 12px;
    display: flex;
    flex-direction: column;
  }
  .bag__stripe span { flex: 1; }
  .bag__stripe .stripe-black { background: var(--flag-black); }
  .bag__stripe .stripe-yellow { background: var(--flag-yellow); }
  .bag__stripe .stripe-red { background: var(--flag-red); }
  .brand {
    position: absolute;
    top: 88px; left: 0; right: 0;
    text-align: center;
  }
  .brand__mark {
    display: block;
    width: 48px; height: 48px;
    margin: 0 auto 22px;
    border-radius: 50%;
    background: var(--flag-black);
  }
  .brand__name {
    font-weight: 700;
    font-size: 24px;
    color: var(--flag-red);
    line-height: 1;
  }
  .brand__tagline {
    font-size: 7px;
    font-weight: 900;
    letter-spacing: 1.5px;
    color: var(--flag-black);
    margin-top: 3px;
  }
  .valve {
    position: absolute;
    top: 222px; left: 130px;
    width: 40px; height: 40px;
    border-radius: 50%;
    border: 1px solid rgba(255,255,255,.6);
    background: rgba(255,255,255,.15);
  }
  .valve::after {
    content: ""; position: absolute; left: 17px; top: 17px;
    width: 4px; height: 4px; border-radius: 50%; background: var(--flag-black);
  }
  .roast {
    position: absolute;
    top: 365px; left: 0; right: 0;
    text-align: center;
  }
  .roast__title {
    font-family: "Archivo Black", Arial, sans-serif;
    font-style: italic;
    font-size: 27px;
    line-height: 1.1;
    color: var(--flag-yellow);
    text-shadow: 1px 1px 0 var(--flag-black), 2px 2px 3px rgba(0,0,0,.5);
  }
  .roast-scale {
    display: flex;
    justify-content: center;
    gap: 6px;
    margin-top: 8px;
  }
  .roast-scale__step {
    width: 34px;
    display: flex; flex-direction: column; align-items: center;
    font-size: 7.5px; font-style: italic; color: var(--white);
  }
  .roast-scale__step svg { margin-bottom: 3px; }
  .roast-scale__tick { margin-top: 2px; }
  .description {
    position: absolute;
    top: 478px; left: 0; right: 0;
    text-align: center;
    font-size: 9px; font-weight: 700;
    line-height: 1.5;
    color: var(--white);
  }
  .net-weight {
    position: absolute;
    right: 30px; bottom: 40px;
    font-size: 9px;
    color: var(--white);
  }
</style>
</head>
<body>

  <section class="bag bag--dark">
    <div class="bag__landscape" role="img" aria-label="Faded illustration of terraced Ugandan mountain hillsides in dark brown tones"></div>
    <div class="brand">
      <span class="brand__mark"></span>
      <div class="brand__name">Bwerani Ridge</div>
      <div class="brand__tagline">PREMIUM UGANDAN COFFEE</div>
    </div>
    <div class="valve"></div>
    <div class="roast">
      <div class="roast__title">Dark Roast</div>
      <div class="roast-scale">
        <div class="roast-scale__step"><svg width="14" height="14" viewBox="0 0 14 14"><circle cx="7" cy="7" r="6" fill="#ffcf3e" stroke="#fff" stroke-width="1"/><path d="M4 10 L10 4" stroke="#fff" stroke-width="1.2"/></svg>Light</div>
        <div class="roast-scale__step"><svg width="14" height="14" viewBox="0 0 14 14"><circle cx="7" cy="7" r="6" fill="#ec1f27" stroke="#fff" stroke-width="1"/><path d="M4 10 L10 4" stroke="#fff" stroke-width="1.2"/></svg>Medium</div>
        <div class="roast-scale__step"><svg width="14" height="14" viewBox="0 0 14 14"><circle cx="7" cy="7" r="6" fill="#7a1015" stroke="#fff" stroke-width="1"/><path d="M4 10 L10 4" stroke="#fff" stroke-width="1.2"/></svg>Dark
          <svg class="roast-scale__tick" width="12" height="10" viewBox="0 0 12 10"><path d="M1 5 L4.5 8.5 L11 1" fill="none" stroke="#fff" stroke-width="1.4"/></svg></div>
        <div class="roast-scale__step"><svg width="14" height="14" viewBox="0 0 14 14"><circle cx="7" cy="7" r="6" fill="#161616" stroke="#fff" stroke-width="1"/><path d="M4 10 L10 4" stroke="#fff" stroke-width="1.2"/></svg>Very Dark</div>
      </div>
    </div>
    <p class="description">A bold, rich Arabica dark roast<br>with hints of vanilla and almond.</p>
    <div class="net-weight">250g | 9oz</div>
    <div class="bag__stripe"><span class="stripe-black"></span><span class="stripe-yellow"></span><span class="stripe-red"></span></div>
  </section>

  <section class="bag bag--light">
    <div class="bag__landscape" role="img" aria-label="Faded illustration of terraced Ugandan mountain hillsides in warm tan tones"></div>
    <div class="brand">
      <span class="brand__mark"></span>
      <div class="brand__name">Bwerani Ridge</div>
      <div class="brand__tagline">PREMIUM UGANDAN COFFEE</div>
    </div>
    <div class="valve"></div>
    <div class="roast">
      <div class="roast__title">Light Roast</div>
      <div class="roast-scale">
        <div class="roast-scale__step"><svg width="14" height="14" viewBox="0 0 14 14"><circle cx="7" cy="7" r="6" fill="#ffcf3e" stroke="#fff" stroke-width="1"/><path d="M4 10 L10 4" stroke="#fff" stroke-width="1.2"/></svg>Light
          <svg class="roast-scale__tick" width="12" height="10" viewBox="0 0 12 10"><path d="M1 5 L4.5 8.5 L11 1" fill="none" stroke="#fff" stroke-width="1.4"/></svg></div>
        <div class="roast-scale__step"><svg width="14" height="14" viewBox="0 0 14 14"><circle cx="7" cy="7" r="6" fill="#ec1f27" stroke="#fff" stroke-width="1"/><path d="M4 10 L10 4" stroke="#fff" stroke-width="1.2"/></svg>Medium</div>
        <div class="roast-scale__step"><svg width="14" height="14" viewBox="0 0 14 14"><circle cx="7" cy="7" r="6" fill="#7a1015" stroke="#fff" stroke-width="1"/><path d="M4 10 L10 4" stroke="#fff" stroke-width="1.2"/></svg>Dark</div>
        <div class="roast-scale__step"><svg width="14" height="14" viewBox="0 0 14 14"><circle cx="7" cy="7" r="6" fill="#161616" stroke="#fff" stroke-width="1"/><path d="M4 10 L10 4" stroke="#fff" stroke-width="1.2"/></svg>Very Dark</div>
      </div>
    </div>
    <p class="description">A bright, smooth Arabica light roast<br>with hints of vanilla and almond.</p>
    <div class="net-weight">250g | 9oz</div>
    <div class="bag__stripe"><span class="stripe-black"></span><span class="stripe-yellow"></span><span class="stripe-red"></span></div>
  </section>

</body>
</html>
```